Tolvern Business Cards

Business card design. dont mind if new logo is suggested.
it would be for a security company.
our clients would be bigger security companies around Australia.
have a logo done but can be replaced. see attaached. like the colors.
Need company name, person name, designation, phone and email on front.
At back company logo and name. website saddress and 2 x license numbers
would like to have 2 different background color for both sidde

Industry/Entity Type

Security

Contact Information for Business Card

round corners, front should be light in color. need logo at back with webaddress and 2 x license numners

Font styles to use
Sans Serif

Colors
f37122
faa54b
f8ba93
0255a3
0592cd
85cae6
b3d448
9bcb3c
ffffff

Requirements
Must have
• see description
Nice to have
• see description
Should not have
• should not be difficult to read or hardd to find information on card.. lets say easy on eyes yet catchy

```html
<!DOCTYPE html>
<html lang="en">
<head>
<meta charset="utf-8">
<title>Tolvern Security Group – Business Cards</title>
<link rel="stylesheet" href="https://fonts.googleapis.com/css2?family=Michroma&family=Roboto:wght@400;500&display=swap">
<style>
  :root {
    --navy: #1f3366;
    --navy-soft: #33487e;
    --cyan: #0aa6cc;
    --ink: #1b1b1b;
    --white: #ffffff;
    --stage: #3a3a3c;
  }
  * { box-sizing: border-box; margin: 0; padding: 0; }
  html, body { width: 1200px; height: 900px; overflow: hidden; }
  body {
    background: var(--stage);
    font-family: "Roboto", Arial, sans-serif;
    position: relative;
  }
  .card {
    position: absolute;
    left: 280px;
    width: 640px;
    height: 366px;
    border-radius: 26px;
    overflow: hidden;
  }

  /* Back side */
  .card-back { top: 40px; background: var(--navy); }
  .back-decor {
    position: absolute; right: 0; top: 0; width: 230px; height: 250px;
    background: radial-gradient(circle at 60% 40%, rgba(120,140,200,0.45), rgba(31,51,102,0) 70%);
  }
  .brand {
    position: absolute; left: 0; right: 0; top: 78px;
    display: flex; flex-direction: column; align-items: center; gap: 18px;
  }
  .brand-mark { width: 56px; height: 56px; border-radius: 50%; background: var(--white); }
  .brand-name {
    color: var(--white); font-weight: 500; font-size: 30px; letter-spacing: 2px;
  }
  .license-band {
    position: absolute; left: 34px; right: 34px; bottom: 46px; height: 44px;
    background: var(--white);
    display: flex; align-items: center; justify-content: center;
    color: var(--navy); font-size: 16px; letter-spacing: 0.5px;
  }

  /* Front side */
  .card-front { top: 466px; background: var(--white); }
  .front-decor {
    position: absolute; left: 0; top: 0; width: 300px; height: 100%;
    background: radial-gradient(circle at 45% 50%, rgba(255,255,255,1) 18%, rgba(10,166,204,0.55) 45%, rgba(31,51,102,0.85) 75%, rgba(255,255,255,0) 100%);
  }
  .details { position: absolute; left: 330px; top: 92px; color: var(--ink); }
  .person-name { font-family: "Michroma", sans-serif; font-size: 22px; letter-spacing: 1px; }
  .person-role { font-family: "Michroma", sans-serif; font-size: 15px; color: var(--cyan); margin-top: 4px; letter-spacing: 1px; }
  .address { font-size: 16px; line-height: 1.3; margin-top: 14px; }
  .contact-list { list-style: none; margin-top: 10px; font-size: 16px; }
  .contact-list li { display: flex; align-items: center; gap: 9px; line-height: 1.55; }
  .contact-list svg { width: 16px; height: 16px; flex: none; }
</style>
</head>
<body>
  <section class="card card-back">
    <div class="back-decor" role="img" aria-label="Faint scattered circle pattern in soft navy tones"></div>
    <div class="brand">
      <div class="brand-mark"></div>
      <div class="brand-name">TOLVERN SECURITY GROUP</div>
    </div>
    <div class="license-band">license no. 204817 | 55120943</div>
  </section>

  <section class="card card-front">
    <div class="front-decor" role="img" aria-label="Large ring of scattered dots in navy and cyan"></div>
    <div class="details">
      <h1 class="person-name">OWEN HARTLEY</h1>
      <p class="person-role">MANAGING DIRECTOR</p>
      <p class="address">14 carrow lane<br>NSW 2700</p>
      <ul class="contact-list">
        <li>
          <svg viewBox="0 0 16 16" aria-hidden="true"><path fill="#0aa6cc" d="M3.5 1.5l2.5 0 1 3.5-1.6 1.2c.8 1.8 2.2 3.2 4 4l1.2-1.6 3.5 1v2.5c0 .8-.7 1.4-1.5 1.4C7 13.5 2.5 9 2.1 3c0-.8.6-1.5 1.4-1.5z"/></svg>
          0491-570-118
        </li>
        <li>
          <svg viewBox="0 0 16 16" aria-hidden="true"><rect x="1" y="3" width="14" height="10" fill="#0aa6cc"/><path d="M1.5 3.5L8 9l6.5-5.5" fill="none" stroke="#fff" stroke-width="1.3"/></svg>
          owen@tolvernsecurity.com.au
        </li>
        <li>
          <svg viewBox="0 0 16 16" aria-hidden="true"><g fill="none" stroke="#0aa6cc" stroke-width="1.3"><circle cx="8" cy="8" r="6.5"/><ellipse cx="8" cy="8" rx="3" ry="6.5"/><path d="M1.5 8h13M2.5 4.8h11M2.5 11.2h11"/></g></svg>
          www.tolvernsecurity.com.au
        </li>
      </ul>
    </div>
  </section>
</body>
</html>
```